Mobile technology Business Card Design Project

We need a business card design for our company based in Sydeny Australia, that takes a company's desktop sites and creates a mobile site compatible to all mobile/smartphone devices. This allows greater ease of use and generally faster business conversion than customers using a desktop site.
Our company is called Zelvora but we refer to it as Zelvora Solutions. If this could be represented somewhere on the business card that would be great.
Am open to suggestions regarding the colours but a high tech  theme would be good.
Happy bidding!

Target Market(s)
Business owner that has a website and is reasonably savvy regarding online/mobile marketing.
Industry/Entity Type
Business
Requirements
Must have
- Business card details:
Director Peter Hawkley
Address: 4/15 Brenton rd, Kelmore. 2047
Email: tbc
Web: www.zelvora-example.com.au
The cards need to have two different names for the two directors.
Damien Ferrowe & Peter Hawkley (two separate business cards)

```html
<!DOCTYPE html>
<html lang="en">
<head>
<meta charset="UTF-8">
<title>Zelvora Business Card</title>
<link href="https://fonts.googleapis.com/css2?family=Questrial&display=swap" rel="stylesheet">
<style>
  :root {
    --page-bg: #e9e9ea;
    --card-white: #ffffff;
    --brand-blue: #1e98d5;
    --brand-blue-light: #5fb6e3;
    --brand-orange: #ef8c1e;
    --ink-dark: #1d1d1f;
    --photo-dark: #2a3440;
    --photo-mid: #5d7a93;
    --photo-light: #b9cfe0;
  }
  * { margin: 0; padding: 0; box-sizing: border-box; }
  html, body { width: 1200px; height: 1000px; overflow: hidden; }
  body {
    background: var(--page-bg);
    font-family: "Questrial", "Century Gothic", sans-serif;
    display: flex;
    flex-direction: column;
    align-items: center;
    justify-content: center;
    gap: 40px;
  }
  .card {
    width: 760px;
    height: 434px;
    background: var(--card-white);
    box-shadow: 0 10px 30px rgba(0,0,0,0.18);
    position: relative;
    overflow: hidden;
  }

  /* Back side */
  .card-back {
    display: flex;
    flex-direction: column;
    align-items: center;
    justify-content: center;
  }
  .brand-dot {
    border-radius: 50%;
    background: var(--brand-blue);
  }
  .card-back .brand-dot { width: 150px; height: 150px; margin-bottom: 26px; }
  .brand-name {
    color: var(--ink-dark);
    line-height: 1;
  }
  .card-back .brand-name { font-size: 52px; }
  .brand-tagline {
    color: var(--brand-orange);
    margin-top: 8px;
  }
  .card-back .brand-tagline { font-size: 20px; }

  /* Front side */
  .card-front { display: flex; }
  .front-left {
    width: 252px;
    display: flex;
    flex-direction: column;
  }
  .front-logo {
    height: 262px;
    display: flex;
    flex-direction: column;
    align-items: center;
    justify-content: center;
  }
  .front-logo .brand-dot { width: 118px; height: 118px; margin-bottom: 18px; }
  .front-logo .brand-name { font-size: 40px; }
  .front-logo .brand-tagline { font-size: 15px; margin-top: 6px; }
  .front-photo {
    flex: 1;
    background: linear-gradient(160deg, var(--photo-dark) 0%, var(--photo-mid) 55%, var(--photo-light) 100%);
  }
  .front-right {
    flex: 1;
    display: flex;
    flex-direction: column;
    color: #ffffff;
  }
  .title-band {
    height: 190px;
    background: var(--brand-blue);
    padding: 64px 0 0 32px;
  }
  .job-title { font-size: 30px; line-height: 1; }
  .person-name {
    font-size: 50px;
    letter-spacing: 1px;
    text-transform: uppercase;
    margin-top: 10px;
    line-height: 1;
  }
  .contact-band {
    flex: 1;
    background: linear-gradient(180deg, var(--brand-blue-light) 0%, var(--brand-blue) 100%);
    padding: 32px 0 0 32px;
  }
  .contact-line {
    font-size: 21px;
    line-height: 1;
    margin-bottom: 18px;
  }
</style>
</head>
<body>
  <section class="card card-back" aria-label="Business card back">
    <div class="brand-dot"></div>
    <div class="brand-name">Zelvora</div>
    <div class="brand-tagline">Zelvora Solutions</div>
  </section>

  <section class="card card-front" aria-label="Business card front">
    <div class="front-left">
      <div class="front-logo">
        <div class="brand-dot"></div>
        <div class="brand-name">Zelvora</div>
        <div class="brand-tagline">Zelvora Solutions</div>
      </div>
      <div class="front-photo" role="img" aria-label="Photo of a businessman holding connected mobile devices and a network globe"></div>
    </div>
    <div class="front-right">
      <div class="title-band">
        <div class="job-title">Director</div>
        <div class="person-name">Peter Hawkley</div>
      </div>
      <div class="contact-band">
        <p class="contact-line">4/15 Brenton rd &nbsp;|&nbsp; Kelmore. 2047</p>
        <p class="contact-line">hawkley@zelvora-example.com.au</p>
        <p class="contact-line">www.zelvora-example.com.au</p>
      </div>
    </div>
  </section>
</body>
</html>
```